I need an amazing business card!

I am the principle in my own software company that develops vexPad and mobile applications. I require a great business card design. I've attached my corporate logo (Thanks Tomasz!).
I would like the design to integrate the logo, my name, email address and skype account:
name Brent Halloway
email brenthalloway@zelqor.com
skype brenthalloway.net
I would like the back of the card to have a "write on me area" similar to the "write on me" card on this page, row 6:
http://us.pravik.com/design-templates/business-cards/#industry=Computing%20%26%20IT
As far as the rest - it's all you!
Updates
1) Please add an example telephone number as well.
Industry/Entity Type
Software
Look and feel
Each slider illustrates characteristics of the customer's brand and the style your logo design should communicate.

```html
<!DOCTYPE html>
<html lang="en">
<head>
<meta charset="utf-8">
<title>Brent Halloway — Business Card</title>
<link href="https://fonts.googleapis.com/css2?family=Open+Sans:wght@400;600;700&display=swap" rel="stylesheet">
<style>
  :root {
    --backdrop: #ededed;
    --card-white: #ffffff;
    --brand-green: #7fab3f;
    --brand-green-light: #9dbf5c;
    --brand-green-dark: #72a033;
    --label-grey: #9a9a9a;
    --line-fill: #ececec;
  }
  * { margin: 0; padding: 0; box-sizing: border-box; }
  html, body {
    width: 1200px;
    height: 1001px;
    overflow: hidden;
    background: var(--backdrop);
    font-family: "Open Sans", sans-serif;
  }
  .card-set {
    position: absolute;
    top: 357px;
    left: 60px;
    display: flex;
    gap: 80px;
  }
  .card {
    width: 500px;
    height: 286px;
    position: relative;
    box-shadow: 0 6px 18px rgba(0,0,0,0.12);
  }

  /* Front */
  .card-front { background: var(--card-white); }
  .brand {
    position: absolute;
    left: 42px;
    top: 100px;
    display: flex;
    align-items: center;
    gap: 12px;
  }
  .brand-square {
    width: 40px;
    height: 40px;
    border-radius: 8px;
    background: var(--brand-green);
  }
  .brand-name {
    font-size: 30px;
    font-weight: 600;
    color: var(--brand-green);
    letter-spacing: 0.04em;
  }
  .contact {
    position: absolute;
    left: 238px;
    top: 140px;
  }
  .contact-name {
    font-size: 21px;
    font-weight: 700;
    color: var(--brand-green);
    margin-bottom: 4px;
  }
  .contact-row {
    display: flex;
    font-size: 13px;
    line-height: 16px;
  }
  .contact-label {
    width: 46px;
    color: var(--label-grey);
  }
  .contact-value { color: var(--brand-green); }

  /* Back */
  .card-back {
    background: linear-gradient(135deg, var(--brand-green-light), var(--brand-green-dark));
    padding: 10px 22px 26px 30px;
  }
  .note-title {
    font-size: 14px;
    color: var(--card-white);
    margin-bottom: 6px;
    padding-left: 4px;
  }
  .note-lines { display: flex; flex-direction: column; gap: 9px; }
  .note-line {
    height: 41px;
    background: var(--line-fill);
  }
</style>
</head>
<body>
  <main class="card-set">
    <section class="card card-front">
      <div class="brand">
        <span class="brand-square"></span>
        <span class="brand-name">zelqor</span>
      </div>
      <div class="contact">
        <p class="contact-name">Brent Halloway</p>
        <p class="contact-row"><span class="contact-label">email</span><span class="contact-value">brenthalloway@zelqor.com</span></p>
        <p class="contact-row"><span class="contact-label">skype</span><span class="contact-value">brenthalloway.net</span></p>
      </div>
    </section>

    <section class="card card-back">
      <p class="note-title">Write on me</p>
      <div class="note-lines">
        <div class="note-line"></div>
        <div class="note-line"></div>
        <div class="note-line"></div>
        <div class="note-line"></div>
        <div class="note-line"></div>
      </div>
    </section>
  </main>
</body>
</html>
```